Brindlewood Business Card Design

Small Company
looking to ramp up work need business cards sick of everyone asking for a card
client base is broad.
keep it simple
Just want on the reverse of the card somewhere for me to write details for clients
appointments etc..
want to use the phrase
"Your safe, reliable and trust worthy Tradesmen"

Industry/Entity Type

Business

Contact Information for Business Card

Brindlewood Electrical Solutions Pty Ltd
Director Gregory Brindlewood
email - brindlewoodelectricalsolutions@zentromail.net
Ph - 03 95418276
Mobile - 0417592836
Domestic, Industrial, Commercial & Mining
Electrical, Solar, Communications & Fibre
REC: 41873

```html
<!DOCTYPE html>
<html lang="en">
<head>
<meta charset="utf-8">
<title>Brindlewood Electrical Solutions – Business Card</title>
<link rel="stylesheet" href="https://fonts.googleapis.com/css2?family=Quicksand:wght@400;500;700&display=swap">
<style>
  :root {
    --ink-blue: #3b3f9c;
    --accent-red: #e8262d;
    --card-white: #f7f7f5;
    --backdrop: #ddd8d2;
    --rule-grey: #b9b9c9;
  }
  * { margin: 0; padding: 0; box-sizing: border-box; }
  html, body { width: 1200px; height: 800px; overflow: hidden; }
  body {
    background: var(--backdrop);
    font-family: "Quicksand", sans-serif;
    color: var(--ink-blue);
    position: relative;
  }
  .card {
    position: absolute;
    width: 540px;
    height: 330px;
    background: var(--card-white);
    top: 235px;
    box-shadow: 0 2px 6px rgba(0,0,0,0.12);
  }
  .card--front { left: 50px; }
  .card--back { left: 610px; }

  .wordmark {
    position: absolute;
    display: flex;
    align-items: center;
    gap: 10px;
    font-weight: 500;
    color: var(--ink-blue);
  }
  .wordmark__dot {
    width: 14px; height: 14px;
    border-radius: 50%;
    background: var(--accent-red);
    flex: none;
  }
  .wordmark__name { font-size: 34px; line-height: 1; }
  .wordmark__sub { font-size: 13px; letter-spacing: 0.08em; text-transform: uppercase; margin-top: 4px; }

  .card--front .wordmark { left: 150px; top: 32px; }
  .tagline {
    position: absolute;
    left: 150px; top: 100px;
    font-size: 14px;
  }
  .holder-name {
    position: absolute;
    left: 150px; top: 134px;
    font-size: 22px;
    font-weight: 500;
  }
  .holder-role {
    position: absolute;
    left: 210px; top: 164px;
    font-size: 14px;
    font-weight: 700;
    color: var(--accent-red);
  }
  .contact-list {
    position: absolute;
    left: 34px; top: 196px;
    list-style: none;
    font-size: 15px;
    line-height: 1.45;
  }
  .contact-list__label { color: var(--accent-red); font-weight: 700; }
  .licence {
    position: absolute;
    right: 30px; bottom: 22px;
    font-size: 15px;
    font-weight: 500;
  }

  .card--back .wordmark { left: 130px; top: 120px; }
  .services {
    position: absolute;
    left: 40px;
    font-size: 12px;
    text-align: center;
    width: 460px;
  }
  .services--top { top: 40px; }
  .services--bottom { bottom: 40px; }
  .write-field {
    position: absolute;
    left: 40px; top: 214px;
    width: 460px;
    display: flex;
    align-items: flex-end;
    gap: 8px;
    font-size: 12px;
    font-weight: 700;
    color: var(--accent-red);
  }
  .write-field__line { flex: 1; border-bottom: 1px solid var(--rule-grey); height: 12px; }
</style>
</head>
<body>
  <section class="card card--front" aria-label="Business card front">
    <div class="wordmark">
      <span class="wordmark__dot" aria-hidden="true"></span>
      <div>
        <div class="wordmark__name">Brindlewood</div>
        <div class="wordmark__sub">Electrical Solutions Pty Ltd</div>
      </div>
    </div>
    <p class="tagline">Your safe, reliable and trust worthy Tradesmen.</p>
    <p class="holder-name">Gregory Brindlewood</p>
    <p class="holder-role">director</p>
    <ul class="contact-list">
      <li><span class="contact-list__label">email:</span> brindlewoodelectricalsolutions@zentromail.net</li>
      <li><span class="contact-list__label">phone:</span> 03 95418276</li>
      <li><span class="contact-list__label">mobile:</span> 0417592836</li>
    </ul>
    <p class="licence">REC: 41873</p>
  </section>

  <section class="card card--back" aria-label="Business card back">
    <p class="services services--top">Domestic, Industrial, Commercial &amp; Mining</p>
    <div class="wordmark">
      <span class="wordmark__dot" aria-hidden="true"></span>
      <div>
        <div class="wordmark__name">Brindlewood</div>
        <div class="wordmark__sub">Electrical Solutions Pty Ltd</div>
      </div>
    </div>
    <div class="write-field"><span>DATE:</span><span class="write-field__line"></span></div>
    <p class="services services--bottom">Electrical, Solar, Communications &amp; Fibres</p>
  </section>
</body>
</html>
```